Brightpath Dental Studio

Please go to www.brightpathdentalstudio.example and obtain the current company logo.
Doctors name are
Marita Velbonne, DDS
Denis Kalb, DMD
Addresses are
318 Larchmont Ave
Teaneck, NJ 07666
201-555-0147
And
872 14th St.
West New York, NJ 07093
201-555-0182
Theme of the business card should feel modrrn and similar to the website.
Front side should include company logo, doctors name, addresses, phone numbers.
Back of the card should include blank lines for patient's name. Date and time for next scheduled appointment. And notice of 24-hr cancellation courtesy policy.
Dental

```html
<!DOCTYPE html>
<html lang="en">
<head>
<meta charset="utf-8">
<title>Brightpath Dental Studio – Business Card</title>
<link href="https://fonts.googleapis.com/css2?family=Roboto+Condensed:ital,wght@0,400;1,300&family=Source+Sans+3:wght@400&display=swap" rel="stylesheet">
<style>
  :root {
    --paper: #ffffff;
    --ink: #1f1f1f;
    --divider: #9d98c2;
    --brand: #3a3a3a;
    --rule: #8a8a8a;
  }
  html, body {
    margin: 0;
    padding: 0;
    overflow: hidden;
    background: var(--paper);
  }
  .card {
    position: relative;
    width: 1200px;
    height: 468px;
    background: var(--paper);
    color: var(--ink);
    font-family: "Source Sans 3", Arial, sans-serif;
    overflow: hidden;
  }
  .doctors {
    position: absolute;
    left: 86px;
    top: 121px;
    font-size: 19px;
    line-height: 27px;
  }
  .doctors p { margin: 0; }
  .brand {
    position: absolute;
    left: 100px;
    top: 200px;
    width: 172px;
    display: flex;
    align-items: center;
    gap: 8px;
    color: var(--brand);
    font-size: 18px;
    line-height: 22px;
  }
  .brand-dot {
    flex: none;
    width: 14px;
    height: 14px;
    border-radius: 50%;
    background: var(--divider);
  }
  .divider {
    position: absolute;
    left: 294px;
    top: 62px;
    width: 4px;
    height: 260px;
    background: var(--divider);
  }
  .office {
    position: absolute;
    left: 326px;
    font-size: 21px;
    line-height: 28px;
  }
  .office p { margin: 0; }
  .office--wny { top: 102px; }
  .office--teaneck { top: 200px; }
  .appointment {
    position: absolute;
    left: 692px;
    top: 64px;
    width: 460px;
    font-family: "Roboto Condensed", "Arial Narrow", sans-serif;
  }
  .appointment-title {
    margin: 0 0 20px;
    font-size: 29px;
    font-weight: 400;
    line-height: 36px;
  }
  .field-row {
    display: flex;
    height: 34px;
    align-items: flex-end;
  }
  .field {
    display: flex;
    align-items: flex-end;
    flex: 1;
    font-size: 19px;
    font-style: italic;
    font-weight: 300;
    line-height: 24px;
  }
  .field--date { flex: none; width: 228px; }
  .field-line {
    flex: 1;
    margin: 0 14px 5px 6px;
    border-bottom: 1px solid var(--rule);
  }
  .notice {
    margin: 26px 0 0;
    width: 460px;
    text-align: center;
    font-size: 19px;
    font-style: italic;
    font-weight: 300;
    line-height: 27px;
    letter-spacing: -0.3px;
  }
</style>
</head>
<body>
<div class="card">
  <section class="front">
    <div class="doctors">
      <p>Marita Velbonne, DDS</p>
      <p>Denis Kalb, DMD</p>
    </div>
    <div class="brand">
      <span class="brand-dot"></span>
      <span class="brand-name">Brightpath Dental Studio</span>
    </div>
    <div class="divider"></div>
    <div class="office office--wny">
      <p>872 14th St.</p>
      <p>West New York, NJ 07093</p>
      <p>201-555-0182</p>
    </div>
    <div class="office office--teaneck">
      <p>318 Larchmont Ave</p>
      <p>Teaneck, NJ 07666</p>
      <p>201-555-0147</p>
    </div>
  </section>
  <section class="appointment">
    <h2 class="appointment-title">Appointment</h2>
    <div class="field-row">
      <div class="field">Name:<span class="field-line"></span></div>
    </div>
    <div class="field-row">
      <div class="field field--date">Date:<span class="field-line"></span></div>
      <div class="field">Time:<span class="field-line"></span></div>
    </div>
    <div class="field-row">
      <div class="field">Location:<span class="field-line"></span></div>
    </div>
    <p class="notice">If you are unable to keep your appointment, please<br>contact us at least 24 hours in advance.</p>
  </section>
</div>
</body>
</html>
```